Calloway Brothers Civil Construction website design

We want a Bold website to promote our Heavy Civil Construction company, We would like an organic / tangible feel to the site. The pictures will be over saturated so they pop. We need to be able to easliy upload new projects and pictures on a regular basis.
Home page will have a full screen width image, "home page image" with silhouette and logo. It will also have about us area and picture
Page 2 will be Project Gallery with pictures in project folders
Page 3 will be an employment application form and submission
Page 4 will be Contact Us
Construction indusrty
Contractor
Coded - Design and coding required
4 page
- Hypatia Sans Pro Light

```html
<!DOCTYPE html>
<html lang="en">
<head>
<meta charset="utf-8">
<title>Calloway Brothers Civil Construction</title>
<link href="https://fonts.googleapis.com/css2?family=Roboto:wght@400;500;700&family=Open+Sans:wght@400;600&display=swap" rel="stylesheet">
<style>
:root{
  --blue:#3b4fa6;
  --blue-dark:#2e3f8a;
  --ink:#2b2b2b;
  --muted:#6b6b6b;
  --light:#f4f4f4;
  --grey:#e9e9e9;
  --footer:#1e1e1e;
  --footer-bar:#111;
  --white:#fff;
}
*{box-sizing:border-box;margin:0;padding:0}
html,body{width:1200px;height:4772px;overflow:hidden}
body{font-family:"Open Sans",sans-serif;color:var(--ink);background:var(--white);position:relative;font-size:15px;line-height:1.6}
h1,h2,h3,h4{font-family:"Roboto",sans-serif;font-weight:500}
.abs{position:absolute}
.btn{display:inline-block;background:var(--blue);color:var(--white);font-family:"Roboto",sans-serif;font-size:14px;padding:10px 30px;border-radius:3px}
.section-title{font-size:38px;text-align:center;color:var(--ink)}
.photo{position:absolute}

/* header */
.topbar{position:absolute;top:0;left:0;width:1200px;height:128px;background:var(--white)}
.call{left:80px;top:42px;font-size:14px;color:var(--blue);line-height:1.3}
.call b{font-family:"Roboto",sans-serif;font-weight:500;display:block}
.brand{left:480px;top:30px;display:flex;align-items:center;gap:12px}
.brand-mark{width:44px;height:44px;border:3px solid var(--blue)}
.brand-name{font-family:"Roboto",sans-serif;font-weight:700;color:var(--blue);font-size:22px;line-height:1.05;letter-spacing:.5px}
.quote-btn{right:80px;top:42px;border-radius:20px;padding:8px 26px}
.nav{top:128px;left:80px;width:1080px;height:46px;background:var(--blue);display:flex;align-items:center;padding:0 20px;gap:0;z-index:2}
.nav a{color:var(--white);font-family:"Roboto",sans-serif;font-size:14px;padding:0 32px;height:46px;line-height:46px}
.nav a.active{background:rgba(255,255,255,.25)}
.nav svg{margin-left:auto}
.hero{top:128px;left:0;width:1200px;height:612px;background:linear-gradient(160deg,#5f7a86 0%,#3e5a4c 35%,#6d7f6a 60%,#2f3a40 100%)}
.hero-text{top:362px;left:0;width:1200px;text-align:center;color:var(--white)}
.hero-text h1{font-size:44px;line-height:1.15;font-weight:700}
.hero-text p{font-size:14px;width:360px;margin:10px auto 26px;line-height:1.4}

/* about */
.about-title{top:790px;left:0;width:1200px}
.about-copy{top:900px;left:80px;width:520px;font-size:14px;color:var(--muted)}
.about-copy p{margin-bottom:14px}
.feature{display:flex;gap:16px;margin-top:20px}
.feature h3{font-size:21px;color:var(--ink)}
.feature p{margin:0}
.about-frame{top:880px;left:620px;width:520px;height:400px;border:4px solid #bbb}
.about-photo{top:896px;left:636px;width:520px;height:400px;background:linear-gradient(150deg,#a69a7c,#7d6b4d 50%,#5b6b55)}

/* stats */
.stats{top:1380px;left:0;width:1200px;height:260px;background:var(--blue);display:flex;justify-content:center;gap:110px;padding-top:56px;color:var(--white);text-align:center}
.stat strong{display:block;font-family:"Roboto",sans-serif;font-size:40px;font-weight:500;line-height:1.2;margin-top:8px}
.stat span{font-size:20px}

/* heavy */
.heavy{top:1640px;left:0;width:600px;height:520px;background:var(--grey)}
.heavy-copy{top:1760px;left:80px;width:430px;font-size:14px;color:var(--muted)}
.heavy-copy h2{font-size:36px;color:var(--ink);margin-bottom:10px}
.heavy-copy .rule{width:60px;height:3px;background:var(--blue);margin-bottom:26px}
.heavy-copy p{margin-bottom:14px}
.heavy-photo{top:1640px;left:600px;width:600px;height:520px;background:linear-gradient(140deg,#c9c2b2,#b39a3c 45%,#6e6a60)}

/* projects */
.projects-title{top:2206px;left:0;width:1200px}
.project{width:332px;height:252px}
.project-overlay{position:absolute;left:0;bottom:0;width:100%;padding:20px;color:var(--white);background:rgba(0,0,0,.55);height:100%;display:flex;flex-direction:column;justify-content:flex-end}
.project-overlay h4{font-size:20px}
.project-overlay p{font-size:13px;line-height:1.4}
.center-btn{left:0;width:1200px;text-align:center}

/* testimonials */
.testimonials{top:2912px;left:0;width:1200px;height:408px;background:var(--blue);color:var(--white);text-align:center}
.testimonials h2{font-size:38px;margin-top:60px}
.testimonials p.q{width:520px;margin:10px auto 14px;font-size:14px;line-height:1.5}
.client{font-family:"Roboto",sans-serif;font-weight:500;font-size:15px;line-height:1.3}
.client small{display:block;font-family:"Open Sans",sans-serif;font-size:13px;font-weight:400}
.avatars{display:flex;justify-content:center;gap:14px;margin-top:20px}
.avatars span{width:66px;height:66px;border-radius:50%;border:3px solid var(--white);background:#c9b7a5}
.quote-mark{font-family:"Roboto",sans-serif;font-size:70px;line-height:1;position:absolute}

/* blogs */
.blogs-title{top:3368px;left:0;width:1200px}
.blog{width:332px;height:480px;background:var(--light)}
.blog-img{height:222px}
.blog-meta{display:flex;justify-content:space-between;padding:12px 16px;font-size:12px;color:var(--muted);border-bottom:1px solid #ddd}
.blog-body{padding:14px 16px}
.blog-body h4{font-size:20px}
.blog-body p{font-size:14px;color:var(--muted);line-height:1.5;margin:4px 0 10px}
.blog-body a{font-size:14px;color:var(--ink)}

/* contact */
.contact-bg{top:4020px;left:0;width:1200px;height:352px;background:linear-gradient(180deg,#fff 0%,#fff 55%,#eeeef3 80%,#e2e3ec 100%)}
.contact-title{top:4040px;left:0;width:1200px}
.field{position:absolute;background:var(--light);border:1px solid #e2e2e2;font-size:13px;color:#888;padding:12px 16px}
.send{top:4296px;left:548px;padding:8px 40px}

/* footer */
.footer{top:4372px;left:0;width:1200px;height:348px;background:var(--footer);color:#ccc;font-size:14px}
.footer h4{color:var(--white);font-size:17px;margin-bottom:8px}
.footer .col{position:absolute;top:62px}
.footer ul{list-style:none;line-height:1.5}
.footer ul li::before{content:"• "}
.foot-brand{display:flex;align-items:center;gap:10px;margin-bottom:18px}
.foot-brand .brand-mark{border-color:var(--white);width:38px;height:38px}
.foot-brand .brand-name{color:var(--white);font-size:19px}
.foot-contact td{padding:2px 10px 2px 0;vertical-align:top}
.socials{position:absolute;right:80px;top:270px;display:flex;gap:10px}
.socials span{width:28px;height:28px;border-radius:50%;background:var(--blue)}
.copyright{top:4720px;left:0;width:1200px;height:52px;background:var(--footer-bar);color:#aaa;font-size:13px;line-height:52px;padding-left:80px}
</style>
</head>
<body>

<header>
  <div class="topbar">
    <div class="abs call">Call Us Now<b>888-123-4567</b></div>
    <div class="abs brand"><span class="brand-mark"></span><span class="brand-name">CALLOWAY BROTHERS<br>CIVIL CONSTRUCTION</span></div>
    <a class="abs btn quote-btn">Get a Quote</a>
  </div>
  <nav class="abs nav">
    <a class="active">Home</a><a>About Us</a><a>Services</a><a>Projects</a><a>Blogs</a><a>Testimonials</a><a>Careers</a><a>Contact Us</a>
    <svg width="18" height="18" viewBox="0 0 24 24" fill="none" stroke="#fff" stroke-width="2.5"><circle cx="10" cy="10" r="7"/><path d="M15 15l6 6"/></svg>
  </nav>
</header>

<section>
  <div class="photo hero" role="img" aria-label="Aerial photo of a highway interchange with trees, a pond and city traffic"></div>
  <div class="abs hero-text">
    <h1>Welcome To Calloway Brothers<br>Civil Construction</h1>
    <p>Lorem Ipsum is simply dummy text of the printing and typesetting industry.</p>
    <a class="btn">Read More</a>
  </div>
</section>

<section>
  <h2 class="abs section-title about-title">About us</h2>
  <div class="abs about-copy">
    <p>Lorem Ipsum is simply dummy text of the printing and typesetting industry. Lorem Ipsum has been the industry's standard dummy text ever since the 1500s.</p>
    <p>when an unknown printer took a galley of type and scrambled it to make a type specimen book. It has survived not only five centuries, but also the leap into electronic typesetting, remaining essentially unchanged.</p>
    <div class="feature">
      <svg width="34" height="34" viewBox="0 0 24 24" fill="none" stroke="#3b4fa6" stroke-width="1.6"><circle cx="12" cy="7" r="3"/><path d="M5 21v-3a7 7 0 0114 0v3M2 13h4M18 13h4"/></svg>
      <div><h3>Professional Approach</h3><p>Lorem Ipsum is simply dummy text the printing and typesetting is the industry's standard dummy text ever since the 1500s.</p></div>
    </div>
    <div class="feature">
      <svg width="34" height="34" viewBox="0 0 24 24" fill="none" stroke="#3b4fa6" stroke-width="1.6"><circle cx="8" cy="8" r="3"/><circle cx="16" cy="8" r="3"/><path d="M2 20a6 6 0 0112 0M10 20a6 6 0 0112 0"/></svg>
      <div><h3>Professional Team</h3><p>Lorem Ipsum is simply dummy text the printing and typesetting is the industry's standard dummy text ever since the 1500s.</p></div>
    </div>
    <div class="feature">
      <svg width="34" height="34" viewBox="0 0 24 24" fill="none" stroke="#3b4fa6" stroke-width="1.6"><path d="M4 14v-2a8 8 0 0116 0v2"/><rect x="3" y="13" width="4" height="6" rx="1"/><rect x="17" y="13" width="4" height="6" rx="1"/></svg>
      <div><h3>24/7 Support</h3><p>Lorem Ipsum is simply dummy text the printing and typesetting is the industry's standard dummy text ever since the 1500s.</p></div>
    </div>
  </div>
  <div class="abs about-frame"></div>
  <div class="photo about-photo" role="img" aria-label="Excavators working on a dirt construction site"></div>
</section>

<section class="abs stats">
  <div class="stat">
    <svg width="64" height="56" viewBox="0 0 32 28" fill="#fff"><circle cx="16" cy="7" r="5"/><circle cx="6" cy="10" r="3.5"/><circle cx="26" cy="10" r="3.5"/><path d="M7 27a9 9 0 0118 0zM0 25a6 6 0 0110-4v4zM32 25a6 6 0 00-10-4v4z"/></svg>
    <strong>300K</strong><span>Happy Customers</span>
  </div>
  <div class="stat">
    <svg width="64" height="56" viewBox="0 0 32 28" fill="#fff"><path d="M6 14a10 10 0 0120 0h3v3H3v-3z"/><rect x="14" y="4" width="4" height="6"/><rect x="4" y="20" width="24" height="4"/></svg>
    <strong>100</strong><span>Projects Annually</span>
  </div>
  <div class="stat">
    <svg width="64" height="56" viewBox="0 0 32 28" fill="#fff"><path d="M16 1C8 1 2 6 2 12c0 3 2 6 5 8l-1 7 7-5h3c8 0 14-5 14-10S24 1 16 1z"/><rect x="9" y="9" width="14" height="2" fill="#3b4fa6"/><rect x="9" y="13" width="10" height="2" fill="#3b4fa6"/></svg>
    <strong>99%</strong><span>Positive Reviews</span>
  </div>
  <div class="stat">
    <svg width="64" height="56" viewBox="0 0 32 28" fill="#fff"><path d="M9 2h14v8a7 7 0 01-14 0z"/><path d="M9 4H4v3a5 5 0 005 5M23 4h5v3a5 5 0 01-5 5" fill="none" stroke="#fff" stroke-width="2"/><rect x="14" y="16" width="4" height="6"/><rect x="10" y="22" width="12" height="4"/></svg>
    <strong>80</strong><span>Awards</span>
  </div>
</section>

<section>
  <div class="abs heavy"></div>
  <div class="abs heavy-copy">
    <h2>Heavy Civil Construction</h2>
    <div class="rule"></div>
    <p>Lorem Ipsum is simply dummy text of the printing and typesetting industry. Lorem Ipsum has been the industry's.</p>
    <p>when an unknown printer took a galley of type and scrambled it to make a type specimen book. It has survived not only five centuries.</p>
    <a class="btn" style="margin-top:20px">Read More</a>
  </div>
  <div class="photo heavy-photo" role="img" aria-label="Yellow bulldozer pushing earth on a construction site"></div>
</section>

<section>
  <h2 class="abs section-title projects-title">Our Projects</h2>
  <div class="photo project" style="top:2300px;left:80px;background:linear-gradient(150deg,#7b8a93,#6f5b44)" role="img" aria-label="Highway bridge construction"></div>
  <div class="photo project" style="top:2300px;left:434px;background:linear-gradient(150deg,#5a5a5a,#3c3c3c)" role="img" aria-label="Project photo">
    <div class="project-overlay"><h4>Project Title</h4><p>Lorem Ipsum is simply dummy the printing and typesetting.</p></div>
  </div>
  <div class="photo project" style="top:2300px;left:788px;background:linear-gradient(150deg,#8e9aa0,#5d6b57)" role="img" aria-label="Aerial view of a roadway project"></div>
  <div class="photo project" style="top:2576px;left:80px;background:linear-gradient(150deg,#6b5a48,#a08056)" role="img" aria-label="Excavation work at a building site"></div>
  <div class="photo project" style="top:2576px;left:434px;background:linear-gradient(150deg,#8a7a52,#b09a3c)" role="img" aria-label="Heavy equipment on a construction site"></div>
  <div class="photo project" style="top:2576px;left:788px;background:linear-gradient(150deg,#4f6a4c,#7a8a6d)" role="img" aria-label="Aerial view of a completed site with pool"></div>
  <div class="abs center-btn" style="top:2820px"><a class="btn">View More</a></div>
</section>

<section class="abs testimonials">
  <span class="quote-mark" style="left:300px;top:70px">“</span>
  <span class="quote-mark" style="left:840px;top:190px">”</span>
  <h2>Testimonials</h2>
  <p class="q">Lorem Ipsum is simply dummy text of the printing and typesetting industry. Lorem Ipsum has been the industry's standard dummy text ever since the 1500s.</p>
  <div class="client">Client Name<small>Quote</small></div>
  <div class="avatars"><span></span><span></span><span></span></div>
</section>

<section>
  <h2 class="abs section-title blogs-title">Blogs</h2>
  <article class="abs blog" style="top:3440px;left:80px">
    <div class="blog-img" style="background:linear-gradient(150deg,#7b9aa8,#5b7a55)" role="img" aria-label="Aerial photo of a highway with a pond"></div>
    <div class="blog-meta"><span>▣ June 16, 2019</span><span>♡ 20 &nbsp; ✉ 12</span></div>
    <div class="blog-body"><h4>Blog Post Title 01</h4><p>Lorem Ipsum is simply dummy the printing and typesetting.</p><a>Continue... ›</a></div>
  </article>
  <article class="abs blog" style="top:3440px;left:434px">
    <div class="blog-img" style="background:linear-gradient(150deg,#8d7a55,#b59b3d)" role="img" aria-label="Bulldozers on a construction site"></div>
    <div class="blog-meta"><span>▣ June 16, 2019</span><span>♡ 20 &nbsp; ✉ 12</span></div>
    <div class="blog-body"><h4>Blog Post Title 01</h4><p>Lorem Ipsum is simply dummy the printing and typesetting.</p><a>Continue... ›</a></div>
  </article>
  <article class="abs blog" style="top:3440px;left:788px">
    <div class="blog-img" style="background:linear-gradient(150deg,#3f6a45,#7a7064)" role="img" aria-label="Trees beside a paved site"></div>
    <div class="blog-meta"><span>▣ June 16, 2019</span><span>♡ 20 &nbsp; ✉ 12</span></div>
    <div class="blog-body"><h4>Blog Post Title 01</h4><p>Lorem Ipsum is simply dummy the printing and typesetting.</p><a>Continue... ›</a></div>
  </article>
  <div class="abs center-btn" style="top:3964px"><a class="btn">View More</a></div>
</section>

<section>
  <div class="abs contact-bg" role="img" aria-label="Faint city skyline silhouette"></div>
  <h2 class="abs section-title contact-title">Quick Contact</h2>
  <div class="field" style="top:4098px;left:236px;width:236px">Name*</div>
  <div class="field" style="top:4098px;left:482px;width:236px">Phone*</div>
  <div class="field" style="top:4098px;left:728px;width:236px">Email*</div>
  <div class="field" style="top:4156px;left:236px;width:728px;height:124px">Message</div>
  <a class="abs btn send">Send</a>
</section>

<footer>
  <div class="abs footer">
    <div class="col" style="left:80px;width:300px">
      <div class="foot-brand"><span class="brand-mark"></span><span class="brand-name">CALLOWAY BROTHERS<br>CIVIL CONSTRUCTION</span></div>
      <p>Lorem Ipsum is simply dummy text of the printing and typesetting industry.</p>
      <p style="margin-top:14px;color:#fff">Read More ›</p>
    </div>
    <div class="col" style="left:416px">
      <h4>Quick Link</h4>
      <ul><li>Home</li><li>About us</li><li>Services</li><li>Projects</li><li>Blogs</li><li>Careers</li><li>Contact us</li></ul>
    </div>
    <div class="col" style="left:588px">
      <h4>Contact us</h4>
      <table class="foot-contact">
        <tr><td>Address :</td><td>1234 Street,<br>Chicago, USA<br>Zipcode</td></tr>
        <tr><td>Phone :</td><td>+123 456 7890</td></tr>
        <tr><td>E-mail :</td><td>info@callowaybrothers.com</td></tr>
      </table>
    </div>
    <div class="col" style="left:884px;width:236px">
      <h4>Career Opportunity</h4>
      <p>Lorem Ipsum is simply dummy text printing and typesetting industry.</p>
      <a class="btn" style="margin-top:12px;padding:6px 26px">Apply Now</a>
    </div>
    <div class="socials"><span></span><span></span><span></span><span></span></div>
  </div>
  <div class="abs copyright">Copyright©2019, Calloway Brothers Civil Construction. All Rights Reserved.</div>
</footer>

</body>
</html>
```